Willowmere Counseling (Endure - Mend - Flourish) - Double Sided Business Card

I would like a 2-sided business card. Front: Matte Black or Navy with Logo & Tagline. Back: Name, Address, Phone Number, Email, & Website (maybe would like to include a small map pin-pointing location); Prefer front to be a gold/silver foil (iridescent); Back prefer white or light colored background with lettering that is easy to read and simple

Target Market(s)

Individuals & Couples (13 y.o. - ALL Adults); High end clientele

Industry/Entity Type

Licensed Professional Counselor (Mental Health)

Contact Information for Business Card

Name: Willowmere Counseling; Tagline: Endure - Mend - Flourish; Address: 3870 N. Garrick Ave., Suite 214, Fort Worth, TX 76132; Phone: (214) 555-0187; Website: www.WillowmereCounseling.example

Font styles to use
Serif

Requirements
Must have
• Logo on Front (Large) prefer gold/silver foil on a matte dark color (i.e. black, navy, etc.); Back of Card: All other relevant information

```html
<!DOCTYPE html>
<html lang="en">
<head>
<meta charset="utf-8">
<title>Willowmere Counseling – Business Card</title>
<link rel="stylesheet" href="https://fonts.googleapis.com/css2?family=Cinzel:wght@400;600&display=swap">
<style>
  :root {
    --backdrop: #3a3b3e;
    --navy: #1b2036;
    --gold: #c9a043;
    --gold-deep: #b5882c;
    --silver: #c4c6c9;
    --paper: #ffffff;
    --ink: #1b2036;
    --map-tone: #e9ebee;
  }
  * { box-sizing: border-box; margin: 0; padding: 0; }
  html, body {
    width: 1200px; height: 1000px; overflow: hidden;
    background: var(--backdrop);
    font-family: "Cinzel", serif;
  }
  .canvas {
    position: relative; width: 1200px; height: 1000px;
  }
  .card {
    position: absolute; left: 250px; width: 700px; height: 400px;
    border-radius: 28px; overflow: hidden;
    box-shadow: 0 12px 30px rgba(0,0,0,.35);
  }
  /* Front */
  .card-front { top: 60px; background: var(--navy); }
  .front-inner {
    position: absolute; inset: 0;
    display: flex; flex-direction: column; align-items: center; justify-content: center;
  }
  .brand-mark {
    width: 74px; height: 74px; border-radius: 50%;
    border: 3px solid var(--silver); margin-bottom: 26px;
  }
  .brand-name {
    font-weight: 600; font-size: 44px; letter-spacing: 2px;
    color: var(--gold); text-transform: uppercase;
  }
  .brand-rule {
    width: 480px; height: 3px; background: var(--silver); margin: 16px 0 14px;
  }
  .tagline {
    font-weight: 600; font-size: 22px; letter-spacing: 1.5px;
    color: var(--gold); text-transform: uppercase;
  }
  /* Back */
  .card-back { top: 540px; background: var(--paper); }
  .location-map {
    position: absolute; left: 42px; top: 58px; width: 270px; height: 200px;
    background: var(--map-tone); border: 3px solid var(--gold-deep);
  }
  .contact {
    position: absolute; right: 40px; top: 52px; width: 340px; text-align: right;
    color: var(--ink);
  }
  .contact-name { font-weight: 600; font-size: 25px; letter-spacing: .5px; text-transform: uppercase; }
  .contact-role { font-size: 14px; letter-spacing: 1px; margin: 2px 0 26px; }
  .contact-line {
    display: flex; justify-content: flex-end; align-items: center; gap: 10px;
    font-size: 13px; margin-bottom: 12px; text-transform: uppercase; white-space: nowrap;
  }
  .contact-line svg { width: 14px; height: 14px; fill: var(--gold-deep); flex: none; }
  .address-band {
    position: absolute; left: 0; right: 0; top: 282px; height: 56px;
    background: var(--gold-deep); color: var(--paper);
    display: flex; align-items: center; justify-content: center;
    font-size: 16px; letter-spacing: 1.5px; text-transform: uppercase;
  }
</style>
</head>
<body>
<main class="canvas">
  <section class="card card-front">
    <div class="front-inner">
      <div class="brand-mark"></div>
      <h1 class="brand-name">Willowmere Counseling</h1>
      <div class="brand-rule"></div>
      <p class="tagline">Endure - Mend - Flourish</p>
    </div>
  </section>

  <section class="card card-back">
    <div class="location-map" role="img" aria-label="Street map pinpointing the office location"></div>
    <div class="contact">
      <h2 class="contact-name">Willowmere Counseling</h2>
      <p class="contact-role">CEO - Founder</p>
      <p class="contact-line">(214) 555-0187
        <svg viewBox="0 0 24 24"><path d="M6.6 10.8a15.1 15.1 0 0 0 6.6 6.6l2.2-2.2a1 1 0 0 1 1-.25 11.4 11.4 0 0 0 3.6.57 1 1 0 0 1 1 1V20a1 1 0 0 1-1 1A17 17 0 0 1 3 4a1 1 0 0 1 1-1h3.5a1 1 0 0 1 1 1c0 1.25.2 2.45.57 3.6a1 1 0 0 1-.25 1z"/></svg>
      </p>
      <p class="contact-line">info@willowmerecounseling.example
        <svg viewBox="0 0 24 24"><path d="M2 5h20v14H2z M2 5l10 8 10-8" fill="none" stroke="#b5882c" stroke-width="2"/></svg>
      </p>
      <p class="contact-line">www.WillowmereCounseling.example
        <svg viewBox="0 0 24 24"><circle cx="12" cy="12" r="9" fill="none" stroke="#b5882c" stroke-width="2"/><path d="M3 12h18M12 3c3 3 3 15 0 18M12 3c-3 3-3 15 0 18" fill="none" stroke="#b5882c" stroke-width="1.6"/></svg>
      </p>
    </div>
    <div class="address-band">3870 N. Garrick Ave., Suite 214, Fort Worth, TX 76132</div>
  </section>
</main>
</body>
</html>
```